PowerPoint Design for a Biotech Consulting Firm

We need a powerpoint design for a new business based in Philadelphia called VorentaRx. This is a consulting firm that will serve medical diagnostics industry, which is part of the life science/healthcare industry focusing on developing and marketing products that help in early detection, monitoring or management of diseases. Our consulting firm will help medical diagnostic companies to overcome key challenges in designing, evaluating and marketing new products.Our company name is VorentaRx. Vorenta is Latin word for "something", Dx represents diagnostics. The idea behind the name is that we help companies to transform the original, early product ideas ("nothing") into "something" which is a product with full clinical utility that will help to improve health and well-being.The powerpoint should use the visual feel of the logo (attached), be modern, simple and clean looking and represent creativity, innovation, scientific thinking and progress.

Target Market(s)

Biotech

Industry/Entity Type

Biotechnology

Font styles to use
Sans Serif

Colors
0355a3
3276b5
85abd2
cfdeed
ffffff
959595
aaaaaa
cbcbcb
070707

Requirements
Must have
• - look and feel, logo colors
• - multiple slide formats

```html
<!DOCTYPE html>
<html lang="en">
<head>
<meta charset="utf-8">
<title>VorentaRx Presentation Template</title>
<link href="https://fonts.googleapis.com/css2?family=Open+Sans:wght@300;400;600;700&display=swap" rel="stylesheet">
<style>
:root{
  --blue:#2e7fe6;
  --blue-deep:#0355a3;
  --blue-mid:#3276b5;
  --blue-soft:#85abd2;
  --ice:#cfdeed;
  --white:#ffffff;
  --gray:#959595;
  --gray-light:#cbcbcb;
  --ink:#070707;
  --stage:#e6e6e6;
  --gold:#c98a22;
  --umber:#7a6548;
}
*{box-sizing:border-box;margin:0;padding:0}
html,body{width:1200px;height:1069px;overflow:hidden;background:var(--stage)}
body{font-family:'Open Sans',Arial,sans-serif;color:var(--ink)}
.canvas{position:relative;width:1200px;height:1069px;background:var(--stage);overflow:hidden}
.slide{position:absolute;width:250px;height:141px;background:var(--white);overflow:hidden;box-shadow:0 1px 2px rgba(0,0,0,.22)}
.a{position:absolute}
.fill-blue{background:var(--blue)}
.tiny{font-size:3.1px;line-height:4.1px;color:#333}
.tiny.w{color:var(--white)}
.tiny.b{font-weight:700}
.label{font-size:3.6px;font-weight:600;color:var(--blue)}
.label.w{color:var(--white)}
.h-blue{font-weight:600;color:var(--blue)}
.h-white{font-weight:600;color:var(--white)}
.caps{font-weight:700;text-transform:uppercase;letter-spacing:.1px}
.ph{position:absolute}
.ph-blue{background:linear-gradient(135deg,#4c98f2,#1c68d0)}
.ph-office{background:linear-gradient(160deg,#a9b2ba,#56626d)}
.ph-warm{background:linear-gradient(160deg,#cdbfb0,#6b5f55)}
.ph-city{background:linear-gradient(180deg,#5d7796 0%,#8d8f95 55%,#c99a5e 100%)}
.ph-green{background:linear-gradient(160deg,#8aa4c4 0%,#7e9a6e 60%,#3d5060 100%)}
.ph-person{background:linear-gradient(180deg,#cfcfcf,#4c4c4c)}
.ph-desk{background:linear-gradient(150deg,#d9d4cc,#8b8378)}
.circle{border-radius:50%}
.icon{position:absolute;color:var(--blue)}
.icon.w{color:var(--white)}
.tag{position:absolute;background:var(--blue);color:var(--white);font-size:3.2px;font-weight:600;padding:0.6px 3px}
.rule{position:absolute;height:0.6px;background:var(--blue)}
.center{text-align:center}
</style>
</head>
<body>
<svg width="0" height="0" style="position:absolute" aria-hidden="true">
  <defs>
    <symbol id="i-monitor" viewBox="0 0 24 24"><g fill="none" stroke="currentColor" stroke-width="1.3"><rect x="2" y="4" width="20" height="13"/><path d="M9 21h6M12 17v4M5 14l4-4 3 3 5-6 3 3"/></g></symbol>
    <symbol id="i-doc" viewBox="0 0 24 24"><g fill="none" stroke="currentColor" stroke-width="1.3"><rect x="5" y="2" width="14" height="20"/><path d="M8 7h8M8 11h8M8 15h5"/></g></symbol>
    <symbol id="i-bars" viewBox="0 0 24 24"><g fill="none" stroke="currentColor" stroke-width="1.3"><rect x="3" y="3" width="18" height="18"/><path d="M7 17v-4M11 17V9M15 17v-6M18 17V7"/></g></symbol>
    <symbol id="i-cal" viewBox="0 0 24 24"><g fill="none" stroke="currentColor" stroke-width="1.3"><rect x="3" y="5" width="18" height="16"/><path d="M3 10h18M8 3v4M16 3v4M8 14h2M12 14h2M16 14h2M8 17h2M12 17h2"/></g></symbol>
    <symbol id="i-users" viewBox="0 0 24 24"><g fill="currentColor"><circle cx="12" cy="8" r="3"/><circle cx="5" cy="10" r="2.2"/><circle cx="19" cy="10" r="2.2"/><path d="M7 20c0-4 2-6 5-6s5 2 5 6zM1 19c0-3 1.5-5 4-5 1 0 1.8.3 2.4.8C6.6 16 6 17.5 6 19zM23 19c0-3-1.5-5-4-5-1 0-1.8.3-2.4.8.8 1.2 1.4 2.7 1.4 4.2z"/></g></symbol>
    <symbol id="i-lock" viewBox="0 0 24 24"><g fill="currentColor"><path d="M7 10V7a5 5 0 0 1 10 0v3h-2V7a3 3 0 0 0-6 0v3z"/><rect x="5" y="10" width="14" height="11" rx="1"/></g></symbol>
    <symbol id="i-play" viewBox="0 0 24 24"><g fill="none" stroke="currentColor" stroke-width="1.5"><rect x="2" y="4" width="20" height="14"/><path d="M10 8v6l5-3z" fill="currentColor"/><path d="M8 21h8"/></g></symbol>
    <symbol id="i-down" viewBox="0 0 24 24"><g fill="currentColor"><path d="M12 2l9 5v10l-9 5-9-5V7z" opacity=".0"/><path d="M10 3h4v7h4l-6 6-6-6h4z"/><path d="M3 14h4l5 5 5-5h4v7H3z"/></g></symbol>
    <symbol id="i-cap" viewBox="0 0 24 24"><g fill="currentColor"><path d="M12 4l11 5-11 5L1 9z"/><path d="M6 12v4c0 2 3 3 6 3s6-1 6-3v-4l-6 3z"/></g></symbol>
    <symbol id="i-hands" viewBox="0 0 24 24"><g fill="currentColor"><path d="M1 8l5-3 4 3 3-2 4 1 6 2-3 6-4 3-5-1-5-2-5-3z"/></g></symbol>
    <symbol id="i-building" viewBox="0 0 24 24"><g fill="currentColor"><path d="M3 21V9l5-3v15zM9 21V3h8v18zM18 21V10h3v11z"/></g><g fill="#fff"><rect x="11" y="6" width="1.5" height="1.5"/><rect x="14" y="6" width="1.5" height="1.5"/><rect x="11" y="10" width="1.5" height="1.5"/><rect x="14" y="10" width="1.5" height="1.5"/><rect x="11" y="14" width="1.5" height="1.5"/><rect x="14" y="14" width="1.5" height="1.5"/></g></symbol>
    <symbol id="i-bag" viewBox="0 0 24 24"><g fill="currentColor"><path d="M9 3h6l-2 4h-2z"/><circle cx="12" cy="15" r="7"/></g></symbol>
    <symbol id="i-org" viewBox="0 0 24 24"><g fill="none" stroke="currentColor" stroke-width="1.3"><circle cx="12" cy="5" r="2.5"/><circle cx="5" cy="18" r="2.5"/><circle cx="12" cy="18" r="2.5"/><circle cx="19" cy="18" r="2.5"/><path d="M12 8v7M5 15v-3h14v3"/></g></symbol>
    <symbol id="i-quote" viewBox="0 0 24 20"><g fill="currentColor"><path d="M1 20V11C1 5 4 1 10 0v4c-3 1-4 3-4 6h4v10zM14 20V11c0-6 3-10 9-11v4c-3 1-4 3-4 6h4v10z"/></g></symbol>
  </defs>
</svg>

<main class="canvas">

<!-- Row 1 -->
<section class="slide" style="left:58px;top:50px">
  <div class="ph ph-blue" role="img" aria-label="Business handshake photo tinted blue" style="left:0;top:0;width:250px;height:112px"></div>
  <div class="a h-white" style="left:14px;top:58px;font-size:10px">Edit title here</div>
  <div class="a" style="left:14px;top:73px;font-size:5.5px;color:var(--white)">Edit subtitle here</div>
  <div class="a" style="left:12px;top:121px;display:flex;align-items:center;gap:2px">
    <span style="width:9px;height:9px;border:0.6px solid var(--blue-soft);display:inline-block"></span>
    <span style="font-size:3px;color:var(--blue)">VorentaRx</span>
  </div>
  <div class="a" style="right:18px;top:124px;font-size:3.6px;color:var(--blue);font-weight:600">www.VorentaRx.com</div>
</section>

<section class="slide fill-blue" style="left:332px;top:50px">
  <div class="ph ph-office" role="img" aria-label="Photo of two colleagues reviewing documents" style="left:0;top:0;width:126px;height:141px"></div>
  <div class="a h-white" style="left:146px;top:33px;font-size:8.5px">Introduction</div>
  <p class="a tiny w" style="left:146px;top:50px;width:90px">Lorem ipsum dolor sit amet, consectetur adipiscing elit, sed do eiusmod tempor incididunt ut labore et dolore magna aliqua. Lorem ipsum dolor sit amet, consectetur adipiscing elit, sed do eiusmod tempor incididunt ut labore et dolore magna aliqua. Lorem ipsum dolor sit amet, consectetur adipiscing elit, sed do eiusmod tempor incididunt ut labore et dolore magna aliqua.</p>
</section>

<section class="slide" style="left:603px;top:50px">
  <div class="ph ph-green" role="img" aria-label="Photo of a modern office building with trees" style="left:0;top:0;width:250px;height:141px"></div>
  <div class="a" style="left:22px;top:0;width:97px;height:116px;background:var(--white)"></div>
  <div class="a h-blue" style="left:36px;top:18px;font-size:8.5px">About Us</div>
  <p class="a tiny" style="left:36px;top:35px;width:76px">Lorem ipsum dolor sit amet, consectetur adipiscing elit, sed do eiusmod tempor incididunt ut labore et dolore magna aliqua. Lorem ipsum dolor sit amet, consectetur adipiscing elit, sed do eiusmod tempor incididunt ut labore et dolore magna aliqua.</p>
</section>

<section class="slide fill-blue" style="left:876px;top:50px">
  <div class="ph" role="img" aria-label="Photo of a city skyline tinted dark blue" style="left:96px;top:0;width:154px;height:25px;background:linear-gradient(90deg,#1f5fb8,#3d6fa8)"></div>
  <div class="a h-white" style="left:18px;top:30px;font-size:6px">Lorem Ipsum</div>
  <p class="a tiny w" style="left:18px;top:40px;width:54px">Lorem ipsum dolor sit amet, consectetur adipiscing elit, sed do eiusmod tempor incididunt ut labore et dolore magna aliqua. Lorem ipsum dolor sit amet, consectetur adipiscing elit, sed do eiusmod tempor incididunt ut labore et dolore magna aliqua. Lorem ipsum dolor sit amet, consectetur adipiscing elit, sed do eiusmod tempor incididunt ut labore et dolore magna aliqua.</p>
  <div class="a" style="left:73px;top:25px;width:157px;height:96px;background:var(--white)"></div>
  <svg class="icon" style="left:93px;top:36px" width="8" height="8"><use href="#i-monitor"/></svg>
  <div class="a label" style="left:93px;top:50px">Lorem Ipsum</div>
  <p class="a tiny" style="left:93px;top:56px;width:50px">Lorem ipsum dolor sit amet, consectetur adipiscing elit.</p>
  <svg class="icon" style="left:165px;top:36px" width="8" height="8"><use href="#i-bars"/></svg>
  <div class="a label" style="left:165px;top:50px">Lorem Ipsum</div>
  <p class="a tiny" style="left:165px;top:56px;width:50px">Lorem ipsum dolor sit amet, consectetur adipiscing elit.</p>
  <svg class="icon" style="left:93px;top:79px" width="8" height="8"><use href="#i-bag"/></svg>
  <div class="a label" style="left:93px;top:93px">Lorem Ipsum</div>
  <p class="a tiny" style="left:93px;top:99px;width:50px">Lorem ipsum dolor sit amet, consectetur adipiscing elit.</p>
  <svg class="icon" style="left:165px;top:79px" width="8" height="8"><use href="#i-lock"/></svg>
  <div class="a label" style="left:165px;top:93px">Lorem Ipsum</div>
  <p class="a tiny" style="left:165px;top:99px;width:50px">Lorem ipsum dolor sit amet, consectetur adipiscing elit.</p>
</section>

<!-- Row 2 -->
<section class="slide" style="left:58px;top:213px">
  <div class="ph ph-office" role="img" aria-label="Photo of an office workstation with monitors" style="left:0;top:0;width:114px;height:141px"></div>
  <div class="a caps" style="left:157px;top:13px;font-size:6.3px;color:var(--gold)">Our Portfolio</div>
  <svg class="icon" style="left:130px;top:33px" width="20" height="20"><use href="#i-bars"/></svg>
  <div class="a label" style="left:159px;top:33px">Lorem Ipsum</div>
  <p class="a tiny" style="left:159px;top:39px;width:82px">Lorem ipsum dolor sit amet, consectetur adipiscing elit, sed do eiusmod tempor incididunt ut labore et dolore magna aliqua.</p>
  <svg class="icon" style="left:130px;top:68px" width="20" height="20"><use href="#i-cal"/></svg>
  <div class="a label" style="left:159px;top:68px">Lorem Ipsum</div>
  <p class="a tiny" style="left:159px;top:74px;width:82px">Lorem ipsum dolor sit amet, consectetur adipiscing elit, sed do eiusmod tempor incididunt ut labore et dolore magna aliqua.</p>
  <svg class="icon" style="left:130px;top:104px" width="20" height="20"><use href="#i-doc"/></svg>
  <div class="a label" style="left:159px;top:104px">Lorem Ipsum</div>
  <p class="a tiny" style="left:159px;top:110px;width:82px">Lorem ipsum dolor sit amet, consectetur adipiscing elit, sed do eiusmod tempor incididunt ut labore et dolore magna aliqua.</p>
</section>

<section class="slide" style="left:332px;top:213px">
  <div class="ph ph-blue" role="img" aria-label="Photo of an empty meeting room tinted blue" style="left:0;top:0;width:250px;height:67px"></div>
  <p class="a center" style="left:20px;top:26px;width:210px;font-size:5.6px;line-height:7.5px;color:var(--white)">“Lorem ipsum dolor sit amet, consectetur adipiscing elit. Phasellus sodales, ligula ultrices tempus ristique, tellus justo aliquam dui,</p>
  <svg class="icon" style="left:44px;top:76px" width="22" height="22"><use href="#i-monitor"/></svg>
  <svg class="icon" style="left:114px;top:76px" width="22" height="22"><use href="#i-bars"/></svg>
  <svg class="icon" style="left:184px;top:76px" width="22" height="22"><use href="#i-doc"/></svg>
  <div class="a label center" style="left:25px;top:103px;width:60px">Lorem Ipsum</div>
  <div class="a label center" style="left:95px;top:103px;width:60px">Lorem Ipsum</div>
  <div class="a label center" style="left:165px;top:103px;width:60px">Lorem Ipsum</div>
  <p class="a tiny center" style="left:25px;top:110px;width:60px">Lorem ipsum dolor sit amet, consectetur adipiscing elit.</p>
  <p class="a tiny center" style="left:95px;top:110px;width:60px">Lorem ipsum dolor sit amet, consectetur adipiscing elit.</p>
  <p class="a tiny center" style="left:165px;top:110px;width:60px">Lorem ipsum dolor sit amet, consectetur adipiscing elit.</p>
</section>

<section class="slide" style="left:603px;top:213px">
  <div class="ph ph-desk" role="img" aria-label="Photo collage of people working at desks" style="left:0;top:0;width:61px;height:45px"></div>
  <div class="ph ph-office" role="img" aria-label="Photo of a team meeting" style="left:62px;top:0;width:61px;height:45px"></div>
  <div class="ph ph-warm" role="img" aria-label="Photo of colleagues talking" style="left:0;top:46px;width:48px;height:48px"></div>
  <div class="ph ph-desk" role="img" aria-label="Photo of a laptop workspace" style="left:49px;top:46px;width:74px;height:48px"></div>
  <div class="ph ph-office" role="img" aria-label="Photo of a man at a computer" style="left:0;top:95px;width:60px;height:46px"></div>
  <div class="ph ph-warm" role="img" aria-label="Photo of a smiling businesswoman" style="left:61px;top:95px;width:62px;height:46px"></div>
  <div class="a h-blue" style="left:173px;top:19px;font-size:7px">Lorem Ipsum</div>
  <p class="a tiny center" style="left:160px;top:35px;width:82px">Lorem ipsum dolor sit amet, consectetur adipiscing elit, sed do eiusmod tempor incididunt ut labore et dolore magna aliqua. Lorem ipsum dolor sit amet, consectetur adipiscing elit, sed do eiusmod tempor incididunt ut labore et dolore magna aliqua. Lorem ipsum dolor sit amet, consectetur adipiscing elit, sed do eiusmod tempor incididunt ut labore et dolore magna aliqua. Lorem ipsum dolor sit amet, consectetur adipiscing elit, sed do eiusmod tempor incididunt ut labore et dolore magna aliqua.</p>
</section>

<section class="slide" style="left:876px;top:213px">
  <div class="a caps" style="left:15px;top:9px;font-size:6px;color:var(--umber)">Meet Our Team</div>
  <div class="ph ph-person" role="img" aria-label="Portrait of team member" style="left:15px;top:29px;width:34px;height:75px"></div>
  <div class="ph ph-person" role="img" aria-label="Portrait of team member" style="left:52px;top:29px;width:34px;height:75px"></div>
  <div class="ph ph-person" role="img" aria-label="Portrait of team member" style="left:89px;top:29px;width:34px;height:75px"></div>
  <div class="ph ph-person" role="img" aria-label="Portrait of team member" style="left:126px;top:29px;width:34px;height:75px"></div>
  <div class="ph ph-person" role="img" aria-label="Portrait of team member" style="left:163px;top:29px;width:34px;height:75px"></div>
  <div class="ph ph-person" role="img" aria-label="Portrait of team member" style="left:200px;top:29px;width:34px;height:75px"></div>
  <div class="a fill-blue center" style="left:15px;top:104px;width:34px;height:14px;color:#fff;font-size:3.4px;padding-top:2px">Adrian Vell<br><span style="font-size:2.7px">CEO/President</span></div>
  <div class="a fill-blue center" style="left:52px;top:104px;width:34px;height:14px;color:#fff;font-size:3.4px;padding-top:2px">Lena Morrow<br><span style="font-size:2.7px">VP Finance</span></div>
  <div class="a fill-blue center" style="left:89px;top:104px;width:34px;height:14px;color:#fff;font-size:3.4px;padding-top:2px">Tessa Quill<br><span style="font-size:2.7px">Human Resource</span></div>
  <div class="a fill-blue center" style="left:126px;top:104px;width:34px;height:14px;color:#fff;font-size:3.4px;padding-top:2px">Mira Halden<br><span style="font-size:2.7px">Managing Director</span></div>
  <div class="a fill-blue center" style="left:163px;top:104px;width:34px;height:14px;color:#fff;font-size:3.4px;padding-top:2px">Joel Brandt<br><span style="font-size:2.7px">Manager Delivery</span></div>
  <div class="a fill-blue center" style="left:200px;top:104px;width:34px;height:14px;color:#fff;font-size:3.4px;padding-top:2px">Owen Tarr<br><span style="font-size:2.7px">Manager Accounts</span></div>
</section>

<!-- Row 3 -->
<section class="slide" style="left:58px;top:378px">
  <div class="a caps" style="left:15px;top:9px;font-size:6.3px;color:var(--blue)">Our Services</div>
  <svg class="icon" style="left:15px;top:33px" width="17" height="17"><use href="#i-monitor"/></svg>
  <div class="a label" style="left:38px;top:34px;font-size:3px">Lorem ipsum dolor</div>
  <p class="a tiny" style="left:38px;top:39px;width:40px">Lorem ipsum dolor sit amet, consectetur adipiscing elit.</p>
  <svg class="icon" style="left:88px;top:33px" width="17" height="17"><use href="#i-bars"/></svg>
  <div class="a label" style="left:111px;top:34px;font-size:3px">Lorem ipsum dolor</div>
  <p class="a tiny" style="left:111px;top:39px;width:40px">Lorem ipsum dolor sit amet, consectetur adipiscing elit.</p>
  <svg class="icon" style="left:15px;top:67px" width="17" height="17"><use href="#i-cal"/></svg>
  <div class="a label" style="left:38px;top:68px;font-size:3px">Lorem ipsum dolor</div>
  <p class="a tiny" style="left:38px;top:73px;width:40px">Lorem ipsum dolor sit amet, consectetur adipiscing elit.</p>
  <svg class="icon" style="left:88px;top:67px" width="17" height="17"><use href="#i-monitor"/></svg>
  <div class="a label" style="left:111px;top:68px;font-size:3px">Lorem ipsum dolor</div>
  <p class="a tiny" style="left:111px;top:73px;width:40px">Lorem ipsum dolor sit amet, consectetur adipiscing elit.</p>
  <svg class="icon" style="left:15px;top:103px" width="17" height="17"><use href="#i-doc"/></svg>
  <div class="a label" style="left:38px;top:104px;font-size:3px">Lorem ipsum dolor</div>
  <p class="a tiny" style="left:38px;top:109px;width:40px">Lorem ipsum dolor sit amet, consectetur adipiscing elit.</p>
  <svg class="icon" style="left:88px;top:103px" width="17" height="17"><use href="#i-org"/></svg>
  <div class="a label" style="left:111px;top:104px;font-size:3px">Lorem ipsum dolor</div>
  <p class="a tiny" style="left:111px;top:109px;width:40px">Lorem ipsum dolor sit amet, consectetur adipiscing elit.</p>
  <div class="ph ph-office" role="img" aria-label="Photo of a business meeting around a table" style="left:161px;top:25px;width:83px;height:100px"></div>
</section>

<section class="slide" style="left:332px;top:378px">
  <div class="a fill-blue" style="left:0;top:0;width:104px;height:141px"></div>
  <svg class="icon w" style="left:43px;top:24px" width="18" height="15"><use href="#i-quote"/></svg>
  <p class="a center" style="left:10px;top:51px;width:84px;font-size:5.2px;line-height:6.8px;font-weight:700;color:#fff">“Lorem ipsum dolor sit amet, consectetur adipiscing elit. Phasellus sodales, ligula ultrices tempus ristique, tellus justo aliquam dui, nec Lorem ipsum dolor sit amet, consectetur</p>
  <div class="a caps" style="left:117px;top:10px;font-size:5.5px;color:var(--blue)">Testimonials</div>
  <div class="ph ph-person circle" role="img" aria-label="Client portrait" style="left:118px;top:33px;width:24px;height:24px"></div>
  <div class="a label" style="left:148px;top:34px">Lorem Ipsum</div>
  <p class="a tiny" style="left:148px;top:40px;width:92px">Lorem ipsum dolor sit amet, consectetur adipiscing elit, sed do eiusmod tempor incididunt ut labore et dolore magna aliqua.</p>
  <div class="ph ph-person circle" role="img" aria-label="Client portrait" style="left:118px;top:70px;width:24px;height:24px"></div>
  <div class="a label" style="left:148px;top:70px">Lorem Ipsum</div>
  <p class="a tiny" style="left:148px;top:76px;width:92px">Lorem ipsum dolor sit amet, consectetur adipiscing elit, sed do eiusmod tempor incididunt ut labore et dolore magna aliqua.</p>
  <div class="ph ph-person circle" role="img" aria-label="Client portrait" style="left:118px;top:105px;width:24px;height:24px"></div>
  <div class="a label" style="left:148px;top:105px">Lorem Ipsum</div>
  <p class="a tiny" style="left:148px;top:111px;width:92px">Lorem ipsum dolor sit amet, consectetur adipiscing elit, sed do eiusmod tempor incididunt ut labore et dolore magna aliqua.</p>
</section>

<section class="slide" style="left:603px;top:378px">
  <div class="a fill-blue" style="left:0;top:0;width:131px;height:141px"></div>
  <div class="a h-white" style="left:17px;top:17px;font-size:7px;line-height:9.5px;width:110px">Lorem ipsum dolor<br>sit amet, consectetur</div>
  <p class="a tiny w b" style="left:17px;top:40px;width:102px">“Lorem ipsum dolor sit amet, consectetur adipiscing elit, sed do eiusmod tempor incididunt ut labore et dolore magna aliqua. Lorem ipsum dolor sit amet, consectetur adipiscing elit, sed do eiusmod tempor incididunt ut labore et dolore magna aliqua. Lorem ipsum dolor sit amet, consectetur adipiscing elit, sed do eiusmod tempor incididunt ut labore et dolore magna aliqua. Lorem ipsum dolor sit amet, consectetur adipiscing elit, sed do eiusmod tempor incididunt ut labore et dolore magna aliqua.</p>
  <svg class="icon" style="left:146px;top:18px" width="12" height="12"><use href="#i-users"/></svg>
  <div class="a label" style="left:170px;top:16px;font-size:3.2px">Lorem ipsum</div>
  <p class="a tiny" style="left:170px;top:22px;width:68px">Lorem ipsum dolor sit amet, consectetur adipiscing elit, sed do eiusmod tempor incididunt ut labore et dolore magna aliqua.</p>
  <svg class="icon" style="left:146px;top:59px" width="12" height="12"><use href="#i-hands"/></svg>
  <div class="a label" style="left:170px;top:57px;font-size:3.2px">Lorem ipsum</div>
  <p class="a tiny" style="left:170px;top:63px;width:68px">Lorem ipsum dolor sit amet, consectetur adipiscing elit, sed do eiusmod tempor incididunt ut labore et dolore magna aliqua.</p>
  <svg class="icon" style="left:146px;top:99px" width="12" height="12"><use href="#i-play"/></svg>
  <div class="a label" style="left:170px;top:97px;font-size:3.2px">Lorem ipsum</div>
  <p class="a tiny" style="left:170px;top:103px;width:68px">Lorem ipsum dolor sit amet, consectetur adipiscing elit, sed do eiusmod tempor incididunt ut labore et dolore magna aliqua.</p>
</section>

<section class="slide" style="left:876px;top:378px">
  <div class="a caps" style="left:15px;top:11px;font-size:6.3px;color:var(--blue)">Edit Title Here</div>
  <div class="ph ph-blue" role="img" aria-label="Office photo tinted blue" style="left:18px;top:31px;width:68px;height:94px"></div>
  <div class="ph ph-blue" role="img" aria-label="Office photo tinted blue" style="left:92px;top:31px;width:68px;height:94px"></div>
  <div class="ph ph-blue" role="img" aria-label="Office photo tinted blue" style="left:166px;top:31px;width:68px;height:94px"></div>
  <svg class="icon w" style="left:42px;top:43px" width="20" height="20"><use href="#i-cal"/></svg>
  <svg class="icon w" style="left:116px;top:43px" width="20" height="20"><use href="#i-monitor"/></svg>
  <svg class="icon w" style="left:190px;top:43px" width="20" height="20"><use href="#i-down"/></svg>
  <div class="a label w center caps" style="left:18px;top:72px;width:68px">Lorem Ipsum Dolor</div>
  <div class="a label w center caps" style="left:92px;top:72px;width:68px">Lorem Ipsum Dolor</div>
  <div class="a label w center caps" style="left:166px;top:72px;width:68px">Lorem Ipsum Dolor</div>
  <p class="a tiny w center" style="left:24px;top:80px;width:56px">“Lorem ipsum dolor sit amet, consectetur adipiscing elit. Phasellus sodales, ligula ultrices tempus.</p>
  <p class="a tiny w center" style="left:98px;top:80px;width:56px">“Lorem ipsum dolor sit amet, consectetur adipiscing elit. Phasellus sodales, ligula ultrices tempus.</p>
  <p class="a tiny w center" style="left:172px;top:80px;width:56px">“Lorem ipsum dolor sit amet, consectetur adipiscing elit. Phasellus sodales, ligula ultrices tempus.</p>
</section>

<!-- Row 4 -->
<section class="slide" style="left:58px;top:542px">
  <div class="ph ph-desk" role="img" aria-label="Photo of a desk seen from above" style="left:14px;top:12px;width:49px;height:52px"></div>
  <div class="ph ph-office" role="img" aria-label="Photo of hands working on papers" style="left:64px;top:12px;width:47px;height:52px"></div>
  <div class="ph ph-warm" role="img" aria-label="Photo of a team at a table" style="left:14px;top:65px;width:49px;height:36px"></div>
  <div class="ph ph-warm" role="img" aria-label="Photo of a cheerful businesswoman" style="left:64px;top:65px;width:47px;height:63px"></div>
  <div class="ph ph-office" role="img" aria-label="Photo of a man at a computer" style="left:14px;top:102px;width:49px;height:26px"></div>
  <div class="a h-blue" style="left:127px;top:22px;font-size:7.3px;line-height:10px">Lorem ipsum dolor<br>sit amet, consectetur</div>
  <p class="a tiny" style="left:127px;top:50px;width:112px">“Lorem ipsum dolor sit amet, consectetur adipiscing elit, sed do eiusmod tempor incididunt ut labore et dolore magna aliqua. Lorem ipsum dolor sit amet, consectetur adipiscing elit, sed do eiusmod tempor incididunt ut labore et dolore magna aliqua. Lorem ipsum dolor sit amet, consectetur adipiscing elit, sed do eiusmod tempor incididunt ut labore et dolore magna aliqua. Lorem ipsum dolor sit amet, consectetur adipiscing elit, sed do eiusmod tempor incididunt ut labore et dolore magna aliqua.</p>
</section>

<section class="slide" style="left:332px;top:542px">
  <div class="a caps center" style="left:0;top:13px;width:250px;font-size:6.8px;color:var(--blue)">Our Team</div>
  <div class="ph ph-person circle" role="img" aria-label="Team member portrait" style="left:22px;top:36px;width:38px;height:38px"></div>
  <div class="ph ph-person circle" role="img" aria-label="Team member portrait" style="left:137px;top:36px;width:38px;height:38px"></div>
  <div class="ph ph-person circle" role="img" aria-label="Team member portrait" style="left:22px;top:84px;width:38px;height:38px"></div>
  <div class="ph ph-person circle" role="img" aria-label="Team member portrait" style="left:137px;top:84px;width:38px;height:38px"></div>
  <div class="tag" style="left:66px;top:38px">Lorem Ipsum</div>
  <p class="a tiny" style="left:66px;top:45px;width:52px">Lorem ipsum dolor sit amet, consectetur adipiscing elit, sed do eiusmod tempor incididunt ut labore et dolore magna aliqua.</p>
  <div class="tag" style="left:181px;top:38px">Lorem Ipsum</div>
  <p class="a tiny" style="left:181px;top:45px;width:52px">Lorem ipsum dolor sit amet, consectetur adipiscing elit, sed do eiusmod tempor incididunt ut labore et dolore magna aliqua.</p>
  <div class="tag" style="left:66px;top:86px">Lorem Ipsum</div>
  <p class="a tiny" style="left:66px;top:93px;width:52px">Lorem ipsum dolor sit amet, consectetur adipiscing elit, sed do eiusmod tempor incididunt ut labore et dolore magna aliqua.</p>
  <div class="tag" style="left:181px;top:86px">Lorem Ipsum</div>
  <p class="a tiny" style="left:181px;top:93px;width:52px">Lorem ipsum dolor sit amet, consectetur adipiscing elit, sed do eiusmod tempor incididunt ut labore et dolore magna aliqua.</p>
</section>

<section class="slide" style="left:603px;top:542px">
  <div class="ph ph-blue" role="img" aria-label="Photo of colleagues in an office tinted blue" style="left:18px;top:0;width:220px;height:65px"></div>
  <div class="rule" style="left:16px;top:84px;width:68px"></div>
  <p class="a h-blue" style="left:16px;top:90px;width:70px;font-size:5.6px;line-height:7.5px;font-weight:400">“Lorem ipsum dolor sit amet, consectetur</p>
  <div class="rule" style="left:16px;top:118px;width:68px"></div>
  <p class="a tiny" style="left:92px;top:79px;width:146px">“Lorem ipsum dolor sit amet, consectetur adipiscing elit, sed do eiusmod tempor incididunt ut labore et dolore magna aliqua. Lorem ipsum dolor sit amet, consectetur adipiscing elit, sed do eiusmod tempor incididunt ut labore et dolore magna aliqua. Lorem ipsum dolor sit amet, consectetur adipiscing elit, sed do eiusmod tempor incididunt ut labore et dolore magna aliqua. Lorem ipsum dolor sit amet, consectetur adipiscing elit, sed do eiusmod tempor incididunt ut labore et dolore magna aliqua.</p>
</section>

<section class="slide" style="left:876px;top:542px">
  <div class="ph" role="img" aria-label="Photo of a laptop on a desk" style="left:0;top:0;width:250px;height:141px;background:linear-gradient(180deg,#8aa3a8,#5e6f73 60%,#8a8f92)"></div>
  <div class="a fill-blue" style="left:0;top:22px;width:250px;height:96px"></div>
  <div class="a h-white center" style="left:0;top:63px;width:250px;font-size:11.5px">SECTION TITLE HERE</div>
</section>

<!-- Row 5 -->
<section class="slide" style="left:58px;top:704px">
  <div class="a fill-blue" style="left:87px;top:0;width:77px;height:141px"></div>
  <p class="a center" style="left:92px;top:27px;width:67px;font-size:5.8px;line-height:7.3px;color:#fff">“Lorem ipsum dolor sit amet, consectetur adipiscing elit. Phasellus sodales, ligula ultrices tempus ristique, tellus justo aliquam dui,</p>
  <div class="tag" style="left:44px;top:26px">Lorem Ipsum</div>
  <p class="a tiny center" style="left:20px;top:34px;width:62px">Lorem ipsum dolor sit amet, consectetur adipiscing elit, sed do eiusmod tempor incididunt ut labore et dolore magna aliqua.</p>
  <div class="tag" style="left:44px;top:83px">Lorem Ipsum</div>
  <p class="a tiny center" style="left:20px;top:91px;width:62px">Lorem ipsum dolor sit amet, consectetur adipiscing elit, sed do eiusmod tempor incididunt ut labore et dolore magna aliqua.</p>
  <div class="tag" style="left:180px;top:28px">Lorem Ipsum</div>
  <p class="a tiny" style="left:180px;top:36px;width:58px">Lorem ipsum dolor sit amet, consectetur adipiscing elit, sed do eiusmod tempor incididunt ut labore et dolore magna aliqua.</p>
  <div class="tag" style="left:180px;top:85px">Lorem Ipsum</div>
  <p class="a tiny" style="left:180px;top:93px;width:58px">Lorem ipsum dolor sit amet, consectetur adipiscing elit, sed do eiusmod tempor incididunt ut labore et dolore magna aliqua.</p>
</section>

<section class="slide" style="left:332px;top:704px">
  <div class="a caps center" style="left:0;top:13px;width:250px;font-size:6.5px;color:var(--umber)">Our Team</div>
  <div class="ph" role="img" aria-label="Photo of a team working at a table tinted blue" style="left:0;top:29px;width:250px;height:52px;background:linear-gradient(90deg,#2d5f9e,#6d87a6,#2c5d9c)"></div>
  <div class="a fill-blue" style="left:22px;top:60px;width:60px;height:40px"></div>
  <div class="a fill-blue" style="left:92px;top:60px;width:60px;height:40px"></div>
  <div class="a fill-blue" style="left:162px;top:60px;width:60px;height:40px"></div>
  <svg class="icon w" style="left:44px;top:66px" width="16" height="16"><use href="#i-bars"/></svg>
  <svg class="icon w" style="left:114px;top:66px" width="16" height="16"><use href="#i-building"/></svg>
  <svg class="icon w" style="left:184px;top:66px" width="16" height="16"><use href="#i-users"/></svg>
  <div class="a label w center" style="left:22px;top:88px;width:60px;font-size:3.4px">Lorem Ipsum Dolor</div>
  <div class="a label w center" style="left:92px;top:88px;width:60px;font-size:3.4px">Lorem Ipsum Dolor</div>
  <div class="a label w center" style="left:162px;top:88px;width:60px;font-size:3.4px">Lorem Ipsum Dolor</div>
  <p class="a tiny b center" style="left:22px;top:109px;width:60px">Lorem ipsum dolor sit amet, consectetur adipiscing elit, sed do eiusmod tempor incididunt ut</p>
  <p class="a tiny b center" style="left:92px;top:109px;width:60px">Lorem ipsum dolor sit amet, consectetur adipiscing elit, sed do eiusmod tempor incididunt ut</p>
  <p class="a tiny b center" style="left:162px;top:109px;width:60px">Lorem ipsum dolor sit amet, consectetur adipiscing elit, sed do eiusmod tempor incididunt ut</p>
</section>

<section class="slide" style="left:603px;top:704px">
  <p class="a h-blue center" style="left:8px;top:42px;width:50px;font-size:6px;line-height:7.8px;font-weight:400">“Lorem ipsum dolor sit amet, consectetur adipiscing elit.</p>
  <div class="ph ph-warm" role="img" aria-label="Photo of a woman with glasses working on a laptop" style="left:63px;top:0;width:94px;height:141px"></div>
  <svg class="icon" style="left:170px;top:18px" width="10" height="10"><use href="#i-lock"/></svg>
  <div class="a label" style="left:188px;top:16px;font-size:3.2px">Lorem Ipsum Dolor</div>
  <p class="a tiny" style="left:188px;top:22px;width:52px">Lorem ipsum dolor sit amet, consectetur adipiscing elit, sed do eiusmod tempor incididunt ut labore et dolore magna aliqua.</p>
  <svg class="icon" style="left:170px;top:59px" width="10" height="10"><use href="#i-hands"/></svg>
  <div class="a label" style="left:188px;top:57px;font-size:3.2px">Lorem Ipsum Dolor</div>
  <p class="a tiny" style="left:188px;top:63px;width:52px">Lorem ipsum dolor sit amet, consectetur adipiscing elit, sed do eiusmod tempor incididunt ut labore et dolore magna aliqua.</p>
  <svg class="icon" style="left:170px;top:100px" width="10" height="10"><use href="#i-cap"/></svg>
  <div class="a label" style="left:188px;top:98px;font-size:3.2px">Lorem Ipsum Dolor</div>
  <p class="a tiny" style="left:188px;top:104px;width:52px">Lorem ipsum dolor sit amet, consectetur adipiscing elit, sed do eiusmod tempor incididunt ut labore et dolore magna aliqua.</p>
</section>

<section class="slide" style="left:876px;top:704px">
  <p class="a h-blue center" style="left:8px;top:40px;width:46px;font-size:6px;line-height:7.8px;font-weight:400">“Lorem ipsum dolor sit amet, consectetur adipiscing</p>
  <div class="a fill-blue" style="left:58px;top:0;width:80px;height:141px"></div>
  <div class="a label w" style="left:72px;top:16px;font-size:3.2px">Lorem Ipsum Dolor</div>
  <p class="a tiny w" style="left:72px;top:22px;width:56px">Lorem ipsum dolor sit amet, consectetur adipiscing elit, sed do eiusmod tempor incididunt ut labore et dolore magna aliqua.</p>
  <div class="a label w" style="left:72px;top:58px;font-size:3.2px">Lorem Ipsum Dolor</div>
  <p class="a tiny w" style="left:72px;top:64px;width:56px">Lorem ipsum dolor sit amet, consectetur adipiscing elit, sed do eiusmod tempor incididunt ut labore et dolore magna aliqua.</p>
  <div class="a label w" style="left:72px;top:100px;font-size:3.2px">Lorem Ipsum Dolor</div>
  <p class="a tiny w" style="left:72px;top:106px;width:56px">Lorem ipsum dolor sit amet, consectetur adipiscing elit, sed do eiusmod tempor incididunt ut labore et dolore magna aliqua.</p>
  <div class="ph ph-office" role="img" aria-label="Photo of hands using a tablet" style="left:138px;top:0;width:112px;height:141px"></div>
</section>

<!-- Row 6 -->
<section class="slide" style="left:58px;top:871px">
  <div class="ph ph-blue" role="img" aria-label="Office photo tinted blue" style="left:0;top:0;width:133px;height:141px"></div>
  <div class="a h-white" style="left:17px;top:34px;font-size:7px">Lorem ipsum dolor sit</div>
  <p class="a tiny w b" style="left:17px;top:46px;width:104px">Lorem ipsum dolor sit amet, consectetur adipiscing elit, sed do eiusmod tempor incididunt ut labore et dolore magna aliqua. Lorem ipsum dolor sit amet, consectetur adipiscing elit, sed do eiusmod tempor incididunt ut labore et dolore magna aliqua. Lorem ipsum dolor sit amet, consectetur adipiscing elit, sed do eiusmod tempor incididunt ut labore et dolore magna aliqua. Lorem ipsum dolor sit amet, consectetur adipiscing elit, sed do eiusmod tempor incididunt ut labore et dolore magna aliqua. Lorem ipsum dolor sit amet, consectetur adipiscing elit, sed do eiusmod tempor incididunt ut labore et dolore magna aliqua.</p>
  <div class="ph ph-desk" role="img" aria-label="Photo of people working with laptops" style="left:133px;top:0;width:117px;height:141px"></div>
</section>

<section class="slide" style="left:332px;top:871px">
  <div class="a fill-blue" style="left:0;top:0;width:250px;height:45px"></div>
  <div class="a caps" style="left:15px;top:13px;font-size:6.3px;color:#fff">Edit Title Here</div>
  <p class="a tiny w b" style="left:15px;top:25px;width:130px">“Lorem ipsum dolor sit amet, consectetur adipiscing elit, sed do eiusmod tempor incididunt ut labore et dolore magna aliqua.</p>
  <div class="ph ph-city" role="img" aria-label="Photo of a waterfront city skyline" style="left:148px;top:22px;width:90px;height:108px"></div>
  <div class="a" style="left:15px;top:62px;font-size:4.6px;font-weight:600">Lorem ipsum dolor sit amet</div>
  <p class="a tiny" style="left:15px;top:72px;width:125px">Lorem ipsum dolor sit amet, consectetur adipiscing elit, sed do eiusmod tempor incididunt ut labore et dolore magna aliqua. Lorem ipsum dolor sit amet, consectetur adipiscing elit, sed do eiusmod tempor incididunt ut labore et dolore magna aliqua. Lorem ipsum dolor sit amet, consectetur adipiscing elit, sed do eiusmod tempor incididunt ut labore et dolore magna aliqua. Lorem ipsum dolor sit amet, consectetur adipiscing elit, sed do eiusmod tempor incididunt ut labore et dolore magna aliqua.</p>
</section>

<section class="slide" style="left:603px;top:871px">
  <div class="a caps" style="left:15px;top:13px;font-size:6.3px;color:var(--blue)">Edit Title Here</div>
  <div class="ph ph-city" role="img" aria-label="Photo of a city highway at dusk" style="left:16px;top:29px;width:218px;height:65px"></div>
  <svg class="icon" style="left:18px;top:104px" width="13" height="13"><use href="#i-users"/></svg>
  <div class="a label" style="left:42px;top:102px;font-size:3.2px">Lorem Ipsum</div>
  <p class="a tiny" style="left:42px;top:108px;width:75px">Lorem ipsum dolor sit amet, consectetur adipiscing elit, sed do eiusmod tempor incididunt ut labore et dolore magna aliqua.</p>
  <svg class="icon" style="left:131px;top:104px" width="13" height="13"><use href="#i-play"/></svg>
  <div class="a label" style="left:154px;top:102px;font-size:3.2px">Lorem Ipsum</div>
  <p class="a tiny" style="left:154px;top:108px;width:75px">Lorem ipsum dolor sit amet, consectetur adipiscing elit, sed do eiusmod tempor incididunt ut labore et dolore magna aliqua.</p>
</section>

<section class="slide" style="left:876px;top:871px">
  <div class="ph" role="img" aria-label="Photo of glass office towers tinted blue" style="left:0;top:0;width:250px;height:141px;background:linear-gradient(135deg,#1f5fc0,#4b92ee 50%,#2a6fd6)"></div>
  <div class="a center" style="left:0;top:37px;width:250px;font-size:14px;font-weight:300;color:#fff;letter-spacing:.3px">THANK YOU</div>
  <div class="a" style="left:72px;top:59px;width:106px;height:0.6px;background:#fff"></div>
  <div class="a center" style="left:0;top:70px;width:250px;font-size:5.2px;font-weight:700;color:#fff">VorentaRx</div>
  <div class="a center" style="left:0;top:82px;width:250px;font-size:3.6px;line-height:5px;font-weight:600;color:#fff">220 Harbor Lane<br>Philadelphia, PA 19103</div>
  <div class="a center" style="left:0;top:98px;width:250px;font-size:3.6px;font-weight:600;color:#fff">P: 215 555 0142 &nbsp;•&nbsp; www.VorentaRx.com</div>
</section>

</main>
</body>
</html>
```